Corvimo Business Card

Corvimo is a young and energetic software development consultancy. We spend our time on the road working with clients on their sites an meeting new potential customers and employees!

We need a sharp, vibrant and memorable business card that will inspires those that receive it to look after it as it oozes quality and is a nice thing in its own right.

We like bold colours and distinctive design. So show us what you can do.

In terms of information on the card, it would be good to see:

* Our logo (Obviously :) )
* Employee name
* Email
* Website address
* Mobile number
* Full company name (Corvimo ltd)
* Registered company number
* Registered company address

Industry/Entity Type

Software

Requirements
Nice to have
• We are thinking that having a QR Code on the business card could be a good way of adding active marketing. It would be good to see if you are able to merge the kind of element in to your designs!

Maybe something special could be achieved using a visual QR Code like those produced at http://www.pixoranta.example/ ? You have our media so feel free to have a play.

```html
<!DOCTYPE html>
<html lang="en">
<head>
<meta charset="utf-8">
<title>Corvimo Business Card</title>
<link href="https://fonts.googleapis.com/css2?family=Open+Sans:wght@400;600;700&display=swap" rel="stylesheet">
<style>
  :root {
    --brand-red: #c0202e;
    --ink: #3c3c3c;
    --rule-grey: #9a9a9a;
    --card-white: #ffffff;
    --backdrop: #e6e6ea;
  }
  * { margin: 0; padding: 0; box-sizing: border-box; }
  html, body {
    width: 1200px;
    height: 987px;
    overflow: hidden;
    background: var(--backdrop);
    font-family: "Open Sans", Arial, sans-serif;
  }
  .canvas {
    position: relative;
    width: 1200px;
    height: 987px;
  }
  .card {
    position: absolute;
    left: 200px;
    width: 800px;
    height: 457px;
    background: var(--card-white);
    border-radius: 28px;
    box-shadow: 0 6px 18px rgba(0,0,0,0.18);
    overflow: hidden;
  }
  .card--back { top: 24px; }
  .card--front { top: 506px; }

  .wordmark {
    color: var(--brand-red);
    font-weight: 400;
    letter-spacing: 2px;
    line-height: 1;
  }

  /* Back */
  .card--back .wordmark {
    position: absolute;
    left: 0; right: 0;
    top: 160px;
    text-align: center;
    font-size: 96px;
  }
  .back-web {
    position: absolute;
    left: 0; right: 0;
    top: 300px;
    text-align: center;
    font-size: 24px;
    font-weight: 700;
    letter-spacing: 2px;
    color: var(--ink);
  }
  .back-web span { color: var(--brand-red); }

  /* Front */
  .card--front .wordmark {
    position: absolute;
    left: 60px;
    top: 120px;
    font-size: 62px;
  }
  .divider {
    position: absolute;
    left: 432px;
    top: 70px;
    width: 2px;
    height: 210px;
    background: linear-gradient(to bottom, rgba(150,150,150,0), #8a8a8a 50%, rgba(150,150,150,0));
  }
  .contact {
    position: absolute;
    left: 462px;
    top: 70px;
    color: var(--ink);
  }
  .contact__name {
    color: var(--brand-red);
    font-size: 30px;
    font-weight: 700;
    line-height: 1.1;
  }
  .contact__title {
    font-size: 22px;
    line-height: 1.2;
    margin-bottom: 12px;
  }
  .contact__list { list-style: none; }
  .contact__item {
    display: flex;
    align-items: center;
    gap: 10px;
    font-size: 21px;
    line-height: 1.45;
  }
  .contact__item svg { width: 18px; height: 18px; flex: none; }
  .contact__item--plain { padding-left: 28px; }

  .rule {
    position: absolute;
    left: 0; right: 0;
    height: 2px;
    background: var(--rule-grey);
  }
  .rule--top { top: 316px; }
  .rule--bottom { top: 394px; }
  .address-band {
    position: absolute;
    left: 0; right: 0;
    top: 324px;
    height: 62px;
    background: var(--brand-red);
    color: var(--card-white);
    font-size: 21px;
    display: flex;
    align-items: center;
    padding-left: 60px;
  }
</style>
</head>
<body>
<main class="canvas">

  <section class="card card--back" aria-label="Card back">
    <div class="wordmark">CORVIMO</div>
    <div class="back-web">www.<span>corvimo</span>.example</div>
  </section>

  <section class="card card--front" aria-label="Card front">
    <div class="wordmark">CORVIMO</div>
    <div class="divider"></div>

    <div class="contact">
      <div class="contact__name">Your Name</div>
      <div class="contact__title">Title</div>
      <ul class="contact__list">
        <li class="contact__item">
          <svg viewBox="0 0 20 20" aria-hidden="true"><circle cx="10" cy="10" r="9" fill="none" stroke="var(--brand-red)" stroke-width="2"/><path d="M7 5.5l2 2-1 1.5c.6 1.3 1.7 2.4 3 3l1.5-1 2 2-1.5 1.5C9.5 14 6 10.5 5.5 7z" fill="var(--brand-red)"/></svg>
          123-456-7890
        </li>
        <li class="contact__item">
          <svg viewBox="0 0 20 20" aria-hidden="true"><rect x="5" y="1" width="10" height="18" rx="2" fill="var(--brand-red)"/><rect x="7" y="3.5" width="6" height="7" fill="#fff"/><rect x="7" y="12.5" width="6" height="4" fill="#fff" opacity=".6"/></svg>
          123-456-7890
        </li>
        <li class="contact__item">
          <svg viewBox="0 0 20 20" aria-hidden="true"><rect x="1" y="4" width="18" height="12" rx="1.5" fill="var(--brand-red)"/><path d="M2 5l8 6 8-6" fill="none" stroke="#fff" stroke-width="1.6"/></svg>
          info@corvimo.example
        </li>
        <li class="contact__item">
          <svg viewBox="0 0 20 20" aria-hidden="true"><circle cx="10" cy="10" r="9" fill="var(--brand-red)"/><g fill="none" stroke="#fff" stroke-width="1.2"><ellipse cx="10" cy="10" rx="4" ry="9"/><path d="M1 10h18M2.5 5.5h15M2.5 14.5h15"/></g></svg>
          www.corvimo.example
        </li>
      </ul>
    </div>

    <div class="rule rule--top"></div>
    <div class="address-band">00, Complex Name, City, State 0004</div>
    <div class="rule rule--bottom"></div>
  </section>

</main>
</body>
</html>
```